KRL Going Cashless

Hello,
We are a medical office looking to get a flyer created to promote to our patients we will be going "Cashless." Our tagline will be "Cash-Less is Stress-Less"

"Starting in July, to offer you the fastest and most convenient service, we are transitioning to a cashless system. You can now enjoy faster checkout times and greater security with card and contactless payments. More info to come."

I've added two other flyers as sample designs we've used.

Please include logo, addresses, website, phone number

Files to include jpeg, png, pdf (under 5mb), Facebook and Instagram sizing.

Thank you,
Doran

```html
<!DOCTYPE html>
<html lang="en">
<head>
<meta charset="utf-8">
<title>KRL Foot &amp; Ankle – Cashless is Stress Less</title>
<link href="https://fonts.googleapis.com/css2?family=Poppins:wght@300;400;500;700;800&display=swap" rel="stylesheet">
<style>
  :root {
    --orange: #f47d4a;
    --teal: #55c1a6;
    --paper: #fafafa;
    --ink: #333333;
    --white: #ffffff;
    --skin-light: #f6e3da;
    --skin: #eccab8;
    --stone: #2e2e2e;
    --stone-light: #4a4a4a;
  }
  html, body {
    margin: 0;
    padding: 0;
    width: 899px;
    height: 1200px;
    overflow: hidden;
    background: var(--paper);
  }
  .flyer {
    position: relative;
    width: 899px;
    height: 1200px;
    background: var(--paper);
    font-family: "Poppins", sans-serif;
    overflow: hidden;
  }
  .feet-photo {
    position: absolute;
    left: 440px;
    top: 0;
    width: 459px;
    height: 700px;
    background: linear-gradient(135deg, var(--skin-light) 0%, var(--skin) 100%);
  }
  .stones-photo {
    position: absolute;
    left: 452px;
    top: 600px;
    width: 290px;
    height: 195px;
    border-radius: 8px;
    background: linear-gradient(160deg, var(--stone-light) 0%, var(--stone) 100%);
    z-index: 2;
  }
  .brand-mark {
    position: absolute;
    left: 44px;
    top: 50px;
    width: 96px;
    height: 96px;
    background: var(--teal);
  }
  .brand {
    position: absolute;
    right: 208px;
    top: 48px;
    text-align: right;
    color: var(--orange);
    font-weight: 700;
  }
  .brand-name {
    font-size: 62px;
    line-height: 58px;
    letter-spacing: -1.5px;
    margin: 0;
    font-weight: 700;
  }
  .brand-name span { display: block; }
  .brand-web {
    font-size: 26px;
    line-height: 30px;
    margin-top: 4px;
    letter-spacing: -0.5px;
  }
  .tag-box {
    position: absolute;
    left: 44px;
    top: 252px;
    width: 405px;
    height: 85px;
    background: var(--teal);
    border-radius: 5px;
    color: var(--white);
    font-size: 64px;
    font-weight: 500;
    line-height: 88px;
    padding-left: 15px;
    box-sizing: border-box;
    white-space: nowrap;
    z-index: 3;
  }
  .headline {
    position: absolute;
    left: 38px;
    top: 340px;
    margin: 0;
    color: var(--orange);
    font-weight: 800;
    font-size: 114px;
    line-height: 98px;
    letter-spacing: -2px;
    z-index: 3;
  }
  .notice {
    position: absolute;
    left: 42px;
    top: 713px;
    width: 434px;
    height: 449px;
    background: var(--orange);
    border-radius: 5px;
    color: var(--white);
    box-sizing: border-box;
    padding: 14px 0 0 27px;
    z-index: 1;
  }
  .notice-text {
    margin: 0;
    font-weight: 300;
    font-size: 27.5px;
    line-height: 32.5px;
    white-space: nowrap;
    letter-spacing: -0.2px;
  }
  .notice-cta {
    margin: 22px 0 0 4px;
    font-weight: 700;
    font-size: 50px;
    line-height: 54px;
    letter-spacing: -2px;
  }
  .contact {
    position: absolute;
    left: 502px;
    top: 815px;
    width: 357px;
    height: 349px;
    border: 1px solid var(--teal);
    border-radius: 6px;
    box-sizing: border-box;
    color: var(--ink);
    font-style: normal;
    background: var(--white);
  }
  .contact-row {
    position: absolute;
    left: 56px;
    margin: 0;
    font-weight: 300;
    font-size: 20.5px;
    line-height: 23px;
    white-space: nowrap;
  }
  .contact-row svg {
    position: absolute;
    left: -38px;
    top: 2px;
  }
  .contact-phone {
    top: 30px;
    font-weight: 500;
    font-size: 33px;
    line-height: 40px;
  }
  .contact-phone svg { left: -42px; top: 5px; }
  .addr-1 { top: 83px; }
  .addr-2 { top: 155px; }
  .addr-3 { top: 227px; }
  .contact-fax { top: 298px; }
</style>
</head>
<body>
<main class="flyer">
  <div class="feet-photo" role="img" aria-label="Photo of bare feet with hands gently massaging one foot"></div>
  <div class="stones-photo" role="img" aria-label="Photo of stacked black spa stones with a white orchid"></div>

  <header>
    <div class="brand-mark"></div>
    <div class="brand">
      <h1 class="brand-name"><span>KRL</span><span>FOOT &amp; ANKLE</span></h1>
      <div class="brand-web">KRLFOOTCARE.COM</div>
    </div>
  </header>

  <div class="tag-box">Cashless is</div>
  <h2 class="headline">STRESS<br>LESS</h2>

  <section class="notice">
    <p class="notice-text">Starting in July, to offer<br>you the fastest and most<br>convenient service, we are<br>transitioning to a cashless<br>system. You can now enjoy<br>faster checkout times &amp;<br>greater security with card<br>&amp; contactless payments.</p>
    <p class="notice-cta">MORE INFO<br>TO COME!</p>
  </section>

  <address class="contact">
    <p class="contact-row contact-phone">
      <svg width="28" height="28" viewBox="0 0 24 24"><path fill="#f47d4a" d="M6.6 10.8a15.1 15.1 0 0 0 6.6 6.6l2.2-2.2c.3-.3.7-.4 1-.2 1.1.4 2.3.6 3.6.6.6 0 1 .4 1 1V20c0 .6-.4 1-1 1A17 17 0 0 1 3 4c0-.6.4-1 1-1h3.5c.6 0 1 .4 1 1 0 1.3.2 2.5.6 3.6.1.3 0 .7-.2 1l-2.3 2.2z"/></svg>
      555 014 2277
    </p>
    <p class="contact-row addr-1">
      <svg width="16" height="20" viewBox="0 0 16 20"><path fill="#f47d4a" d="M8 0a7 7 0 0 0-7 7c0 5 7 13 7 13s7-8 7-13a7 7 0 0 0-7-7zm0 9.5A2.5 2.5 0 1 1 8 4.5a2.5 2.5 0 0 1 0 5z"/></svg>
      88 Maple Ridge Dr.<br>Ste. 170 Lakeview, MD 20010
    </p>
    <p class="contact-row addr-2">
      <svg width="16" height="20" viewBox="0 0 16 20"><path fill="#f47d4a" d="M8 0a7 7 0 0 0-7 7c0 5 7 13 7 13s7-8 7-13a7 7 0 0 0-7-7zm0 9.5A2.5 2.5 0 1 1 8 4.5a2.5 2.5 0 0 1 0 5z"/></svg>
      2250 Orchard Blvd.<br>Ste. 201 Hillcrest, MD 20020
    </p>
    <p class="contact-row addr-3">
      <svg width="16" height="20" viewBox="0 0 16 20"><path fill="#f47d4a" d="M8 0a7 7 0 0 0-7 7c0 5 7 13 7 13s7-8 7-13a7 7 0 0 0-7-7zm0 9.5A2.5 2.5 0 1 1 8 4.5a2.5 2.5 0 0 1 0 5z"/></svg>
      47 Wellness Way<br>Riverton, WV&nbsp;&nbsp;25030
    </p>
    <p class="contact-row contact-fax">
      <svg width="18" height="18" viewBox="0 0 18 18"><path fill="#f47d4a" d="M0 5h4v13H0zM5 2h8v4H5zM5 7h13v11H5zm3 2v2h2V9zm4 0v2h2V9zm-4 4v2h2v-2zm4 0v2h2v-2z"/></svg>
      555 014 3388
    </p>
  </address>
</main>
</body>
</html>
```